Website for an interior designer

We need a new website for Clara Beth Holloway whose new business name is Clara Beth Holloway Interiors. She is a residential interior designer with a mix of modern and contemporary tastes. We are in the process of overhauling her website which is +15 years old and not an accurate reflection of her tastes. The uploaded photos are from some of the houses she has done as well as her logo(s). We would need a section for "About Us" that would have a paragraph of text and bullets showing services and a gallery for photos (~12 total, more to come). A contract page would be optional. The client likes the feel/look of this website: https://www.pondrickstudio.example/ but doesn't want to copy it exactly.

Target Market(s)

Upscale home owners

Industry/Entity Type

Interior Design

Coding

Coded - Design and coding required

Number of Pages Required

4 page

Colors

Designer to choose only greyscale colors for use in the design.

Requirements
Must have
• Home page, about us page, gallery page, contact us page.

```html
<!DOCTYPE html>
<html lang="en">
<head>
<meta charset="utf-8">
<title>Clara Beth Holloway Interiors</title>
<link href="https://fonts.googleapis.com/css2?family=Playfair+Display:wght@400;500&family=Roboto:wght@300;400;500;700&display=swap" rel="stylesheet">
<style>
:root{
  --ink:#333333;
  --text:#555555;
  --muted:#8a8a8a;
  --rule:#d4d4d4;
  --nav:#c9c9c9;
  --white:#ffffff;
  --dark:#3b3b3b;
  --darker:#333333;
  --field-border:#cfcfcf;
}
*{box-sizing:border-box;margin:0;padding:0}
html,body{width:1200px;height:3849px;overflow:hidden;background:var(--white)}
body{font-family:"Roboto",sans-serif;color:var(--text);position:relative}
h2,h3{font-weight:400}
.abs{position:absolute}

/* header */
.brand{top:0;left:0;width:1200px;height:139px;display:flex;flex-direction:column;align-items:center;justify-content:center;gap:10px}
.brand-mark{width:14px;height:14px;border:1px solid var(--ink);border-radius:50%}
.brand-name{font-family:"Playfair Display",serif;font-size:20px;font-weight:400;letter-spacing:3px;color:var(--ink);text-transform:uppercase}
.topnav{top:139px;left:0;width:1200px;height:63px;background:var(--nav)}
.topnav a,.footnav a{position:absolute;transform:translateX(-50%);text-decoration:none;color:var(--ink);font-size:16px;letter-spacing:.5px;white-space:nowrap}
.topnav a{top:21px}
.topnav .sep{position:absolute;top:20px;width:1px;height:22px;background:#8f8f8f}

/* hero */
.hero{top:202px;left:0;width:1200px;height:632px;background:linear-gradient(180deg,#3d3b48 0%,#3a3845 55%,#5a4a50 80%,#8c6e70 100%)}
.hero-welcome{top:160px;width:1200px;text-align:center;color:var(--white);font-family:"Playfair Display",serif;font-size:38px;letter-spacing:14px}
.hero-title{top:212px;width:1200px;text-align:center;color:var(--white);font-family:"Playfair Display",serif;font-size:64px}
.hero-btn{top:304px;left:490px;width:212px;height:59px;border-radius:30px;background:var(--white);color:var(--ink);font-size:20px;font-weight:500;letter-spacing:.5px;display:flex;align-items:center;justify-content:center}
.hero-arrow{top:295px}
.hero-notch{top:604px;left:555px}

/* about */
.section-title{width:1200px;text-align:center;font-family:"Playfair Display",serif;font-size:40px;font-weight:400;color:var(--ink)}
.section-title .light{color:var(--muted)}
.about-title{top:920px}
.about-rule{top:980px;left:576px;width:48px;height:2px;background:var(--muted)}
.about-copy{top:1005px;left:215px;width:770px;text-align:center;font-size:17.5px;line-height:30px;color:var(--text);font-weight:300}
.outline-btn{border:2px solid var(--muted);border-radius:30px;display:flex;align-items:center;justify-content:center;color:var(--ink);font-size:18px;letter-spacing:.5px}
.about-btn{top:1153px;left:503px;width:193px;height:54px}
.divider{left:67px;width:1069px;height:4px;border-top:1px solid var(--rule);border-bottom:1px solid var(--rule)}

/* services */
.services-title{top:1365px;left:67px;font-family:"Playfair Display",serif;font-size:41px;font-weight:400;color:var(--ink);white-space:nowrap}
.services-title .light{color:var(--muted)}
.services-line{top:1391px;left:356px;width:204px;height:2px;background:var(--muted)}
.services-list{top:1455px;left:72px;list-style:none}
.services-list li{height:45.4px;display:flex;align-items:center;gap:18px;font-size:16px;color:var(--ink);font-weight:300}
.services-photo{top:1334px;left:596px;width:540px;height:398px;background:linear-gradient(180deg,#ecebe8 0%,#e2dfd8 55%,#bfb5a6 85%,#8e7a65 100%)}

/* gallery */
.gallery-title{top:1860px}
.gallery-rule{top:1916px;left:599px;width:2px;height:28px;background:var(--muted)}
.tile{width:336px;height:221px}
.tile-feature{display:flex;flex-direction:column;align-items:center;justify-content:center;color:var(--white);text-align:center;background:linear-gradient(180deg,#5e5a56,#7b7671)}
.tile-feature h3{font-size:19px;font-weight:700;letter-spacing:.5px;margin-bottom:6px}
.tile-feature p{font-size:13.5px;line-height:16px;width:260px;font-weight:300}
.view-btn{top:2937px;left:510px;width:179px;height:57px}

/* contact */
.contact-left{top:3046px;left:0;width:435px;height:535px;background:var(--darker)}
.contact-right{top:3046px;left:435px;width:765px;height:535px;background:var(--dark)}
.contact-title{top:3122px;left:110px;font-family:"Playfair Display",serif;font-size:34px;font-weight:400;color:var(--white);letter-spacing:.5px}
.contact-rule{top:3172px;left:114px;width:48px;height:2px;background:var(--white)}
.ring{width:74px;height:74px;border:2px solid #6a6a6a;border-radius:50%;display:flex;align-items:center;justify-content:center}
.info{width:220px}
.info-label{font-size:18px;font-weight:700;color:var(--white)}
.info-value{font-size:24px;font-weight:700;color:var(--white);margin-top:4px;white-space:nowrap}
.info-value.email{font-size:20px;font-weight:400}
.field{background:var(--white);border:1px solid var(--field-border);color:#8f8f8f;font-size:14px;padding:0 18px;display:flex;align-items:center}
.field.msg{align-items:flex-start;padding-top:18px}
.submit{top:3448px;left:498px;width:170px;height:53px;border:2px solid var(--white);border-radius:30px;color:var(--white);font-size:19px;font-weight:500;display:flex;align-items:center;justify-content:center;letter-spacing:.5px}

/* footer */
.footer-brand{top:3620px;width:1200px;display:flex;justify-content:center;align-items:center;gap:10px}
.footnav a{top:3693px}
.copyright{top:3728px;width:1200px;text-align:center;font-size:14px;color:var(--ink)}
.social{width:36px;height:36px;border:2px solid var(--ink);border-radius:50%;top:3769px}
</style>
</head>
<body>

<header>
  <div class="abs brand">
    <span class="brand-mark"></span>
    <span class="brand-name">Clara Beth Holloway Interiors</span>
  </div>
  <nav class="abs topnav">
    <a style="left:300px">HOME</a><span class="sep" style="left:363px"></span>
    <a style="left:441px">ABOUT US</a><span class="sep" style="left:518px"></span>
    <a style="left:592px">SERVICES</a><span class="sep" style="left:667px"></span>
    <a style="left:740px">GALLERY</a><span class="sep" style="left:810px"></span>
    <a style="left:887px">CONTACT</a>
  </nav>
</header>

<section class="abs hero" role="img" aria-label="Living room with dark paneled wall, two pink velvet armchairs, pendant lamps and side tables with plants">
  <div class="abs hero-welcome">WELCOME TO</div>
  <div class="abs hero-title">CLARA BETH HOLLOWAY</div>
  <div class="abs hero-btn">CONTACT US</div>
  <svg class="abs hero-arrow" style="left:22px" width="26" height="40" viewBox="0 0 26 40"><path d="M20 4 L6 20 L20 36" fill="none" stroke="#fff" stroke-width="2.5"/></svg>
  <svg class="abs hero-arrow" style="left:1142px" width="26" height="40" viewBox="0 0 26 40"><path d="M6 4 L20 20 L6 36" fill="none" stroke="#fff" stroke-width="2.5"/></svg>
  <svg class="abs hero-notch" width="90" height="30" viewBox="0 0 90 30"><path d="M0 30 Q30 30 45 2 Q60 30 90 30 Z" fill="#fff"/><path d="M37 14 L45 21 L53 14" fill="none" stroke="#999" stroke-width="2"/></svg>
</section>

<section>
  <h2 class="abs section-title about-title"><span class="light">ABOUT</span> CLARA BETH HOLLOWAY</h2>
  <div class="abs about-rule"></div>
  <p class="abs about-copy">Clara Beth Holloway has extensive experience in all aspects of interior design. She has worked on a wide array of residential and commercial projects in her hometown of Houston and across the United States. Clara Beth’s taste can best be described as a sophisticated blend of modern and traditional styles that combine to create a clean, timeless space.</p>
  <div class="abs outline-btn about-btn">READ MORE</div>
  <div class="abs divider" style="top:1265px"></div>
</section>

<section>
  <h2 class="abs services-title"><span class="light">OUR</span> SERVICES</h2>
  <div class="abs services-line"></div>
  <ul class="abs services-list">
    <li><svg width="10" height="16" viewBox="0 0 10 16"><path d="M2 2 L8 8 L2 14" fill="none" stroke="#333" stroke-width="1.8"/></svg>Concept Origination and Project Management</li>
    <li><svg width="10" height="16" viewBox="0 0 10 16"><path d="M2 2 L8 8 L2 14" fill="none" stroke="#333" stroke-width="1.8"/></svg>Review of Proposed Plans for New Construction and Remodels</li>
    <li><svg width="10" height="16" viewBox="0 0 10 16"><path d="M2 2 L8 8 L2 14" fill="none" stroke="#333" stroke-width="1.8"/></svg>Procurement of Furniture, Accents, Art, Fixtures and Fittings</li>
    <li><svg width="10" height="16" viewBox="0 0 10 16"><path d="M2 2 L8 8 L2 14" fill="none" stroke="#333" stroke-width="1.8"/></svg>Selection of Paints, Finishes and Construction Materials</li>
    <li><svg width="10" height="16" viewBox="0 0 10 16"><path d="M2 2 L8 8 L2 14" fill="none" stroke="#333" stroke-width="1.8"/></svg>Vendor Coordination and Recommendations</li>
    <li><svg width="10" height="16" viewBox="0 0 10 16"><path d="M2 2 L8 8 L2 14" fill="none" stroke="#333" stroke-width="1.8"/></svg>Home Staging, Styling and Editing</li>
  </ul>
  <div class="abs services-photo" role="img" aria-label="Bright white living room with tall windows, cream sofas and a glass coffee table"></div>
  <div class="abs divider" style="top:1809px"></div>
</section>

<section>
  <h2 class="abs section-title gallery-title"><span class="light">OUR</span> GALLERY</h2>
  <div class="abs gallery-rule"></div>

  <div class="abs tile" style="top:1968px;left:88px;background:linear-gradient(180deg,#3a3330,#6b5448 60%,#8a7a62)" role="img" aria-label="Brick patio with black awning and outdoor dining set"></div>
  <div class="abs tile" style="top:1968px;left:436px;background:linear-gradient(180deg,#e6e8e8,#c9c6c0 60%,#8b8070)" role="img" aria-label="White brick loggia with lanterns and outdoor lounge seating"></div>
  <div class="abs tile" style="top:1968px;left:784px;background:linear-gradient(180deg,#d8d6d2,#eeeeec 50%,#9a9896)" role="img" aria-label="White dining table with white chairs"></div>

  <div class="abs tile" style="top:2201px;left:88px;background:linear-gradient(180deg,#f4f3f1,#e2ddd6 60%,#c8b8a0)" role="img" aria-label="Light living room with grey sofa and wooden armchair"></div>
  <div class="abs tile tile-feature" style="top:2201px;left:436px" role="img" aria-label="Featured project with curved sofa">
    <h3>YOUR PROJECT</h3>
    <p>Augiat in pede Fusce tellus Sed metus augue convallis et vehicula</p>
  </div>
  <div class="abs tile" style="top:2201px;left:784px;background:linear-gradient(180deg,#5c6066,#8a8c8e 55%,#4e5258)" role="img" aria-label="Library sitting room with fireplace and blue armchairs"></div>

  <div class="abs tile" style="top:2434px;left:88px;background:linear-gradient(180deg,#e9e1d4,#d8c8ad 60%,#8c7456)" role="img" aria-label="Cream living room with framed art and wicker trunk"></div>
  <div class="abs tile" style="top:2434px;left:436px;background:linear-gradient(180deg,#e2d8c6,#a8814f 60%,#6c4a2c)" role="img" aria-label="Dining room with wooden table and framed prints"></div>
  <div class="abs tile" style="top:2434px;left:784px;background:linear-gradient(135deg,#3a3430,#c45a86 55%,#e89bbd)" role="img" aria-label="Colorful painted bench in a dark hallway"></div>

  <div class="abs tile" style="top:2667px;left:88px;background:linear-gradient(180deg,#f0ece6,#d9c8ab 60%,#b58d5c)" role="img" aria-label="Open living area with wooden staircase"></div>
  <div class="abs tile" style="top:2667px;left:436px;background:linear-gradient(180deg,#e7e0d6,#b39a7a 60%,#6b5a48)" role="img" aria-label="Breakfast nook with round table and mirror"></div>
  <div class="abs tile" style="top:2667px;left:784px;background:linear-gradient(180deg,#f3f3f2,#e6e4e1 60%,#3b3330)" role="img" aria-label="White entry with staircase and pedestal table"></div>

  <div class="abs outline-btn view-btn">VIEW ALL</div>
</section>

<section>
  <div class="abs contact-left"></div>
  <div class="abs contact-right"></div>
  <h2 class="abs contact-title">CONTACT US</h2>
  <div class="abs contact-rule"></div>

  <div class="abs ring" style="top:3217px;left:105px">
    <svg width="32" height="32" viewBox="0 0 24 24"><path d="M6.5 3.5 L9 3.5 L10.5 8 L8.5 9.5 Q10 13.5 14.5 15.5 L16 13.5 L20.5 15 L20.5 17.5 Q20 20.5 17 20.5 Q5 19 3.5 7 Q3.5 4 6.5 3.5 Z" fill="none" stroke="#fff" stroke-width="1.1"/></svg>
  </div>
  <div class="abs info" style="top:3224px;left:202px">
    <div class="info-label">Phone Number</div>
    <div class="info-value">555 010 4821</div>
  </div>

  <div class="abs ring" style="top:3336px;left:105px">
    <svg width="26" height="20" viewBox="0 0 26 20"><rect x="1" y="1" width="24" height="18" fill="none" stroke="#fff" stroke-width="1.4"/><path d="M1 1 L13 11 L25 1" fill="none" stroke="#fff" stroke-width="1.4"/></svg>
  </div>
  <div class="abs info" style="top:3346px;left:202px">
    <div class="info-label">Email address</div>
    <div class="info-value email">studio@cbh.example</div>
  </div>

  <div class="abs field" style="top:3190px;left:498px;width:309px;height:51px">First Name*</div>
  <div class="abs field" style="top:3190px;left:816px;width:309px;height:51px">Last Name*</div>
  <div class="abs field" style="top:3254px;left:498px;width:309px;height:51px">Email address*</div>
  <div class="abs field" style="top:3254px;left:816px;width:309px;height:51px">Phone*</div>
  <div class="abs field msg" style="top:3320px;left:498px;width:627px;height:110px">Message</div>
  <div class="abs submit">SUBMIT</div>
</section>

<footer>
  <div class="abs footer-brand">
    <span class="brand-name">Clara Beth Holloway Interiors</span>
  </div>
  <nav class="footnav">
    <a style="left:296px">HOME</a>
    <a style="left:436px">ABOUT US</a>
    <a style="left:589px">SERVICES</a>
    <a style="left:737px">GALLERY</a>
    <a style="left:883px">CONTACT</a>
  </nav>
  <div class="abs copyright">© 2020 Clara Beth Holloway | All Rights Reserved</div>
  <div class="abs social" style="left:533px"></div>
  <div class="abs social" style="left:578px"></div>
  <div class="abs social" style="left:623px"></div>
</footer>

</body>
</html>
```